THIS IS A LATIN MUSICAL CD BUT IN ENGLISH THE TITLE WOULD BE “BENEATH THE QUIET RAIN" JUST THAT YOU K

DIGIPACK CD COVER

THIS IS THE INFO NEEDED ON THE FRONT COVER

CD TITLE "BAJO LA LLUVIA SERENA"
ARTIST: ELÍAS MORO

I WOULD NEED A GREAT DESIGN TO WIN A PREMIO SOLAR FOR THIS MUSICAL PROJECT. I WANT A DESIGN THAT MAY CONTAIN TERMS AS HOPE, LOVE , FREEDOM , SALVATION.

I WILL ATTACH THE PRINCIPAL SONG CALL “BENEATH THE QUIET RAIN" MAYBE YOU CAN FIND INSPIRATION AND A PICTURE OF MY GUITAR.

THIS IS THE INFO NEEDED FOR THE BACK COVER , INSIDE COVERS TOO

SONGS:
1 BAJO LA LLUVIA SERENA
2 LUZ EN MI CAMINO
3 CIELO ABIERTO
4 AGUA VIVA Y ETERNA
5 TU PAZ
6 ESPERANZA
7 SOL DE LA MAÑANA
8 TU VOZ ME ALCANZÓ
9 LUZ EN MI CAMINO (DISCO)
10 NUEVO AMANECER
Updates

Hi People i will like to say thanks for be part of this project, the truth is that I do not like to be on the cover of the disc playing my guitar even though I have pictures playing in HD, I would like more a kind of art that reflects peace, hope, salvation , also could be natural landscapes that reflect the title of the album or situations in the real life where the phrase is reflected *beneath the quiet rain*(Album Title) ,or maybe a little child with headphones and looking the sky its just a couple of ideas you can consider, the primary focus is what happens when we hear the name of God , referent to the letters i would like to see fonts more modern . Cheers!!!!! Added Tuesday, June 9, 2015

Project Deadline Extended Reason: im currently working with all of your designs on small details. Once this is done i will have a final decision.Thank you for being part of this project Sincerely,Elias Moro Added Tuesday, June 16, 2015

Target Market(s)

all people who believe in God and not

Industry/Entity Type

Religious

Font styles to use
Serif
Sans Serif
Decorative
Script

Requirements
Must have
• original design , i will like to say thanks for be part of this project, ,I would like more a kind of art that reflects peace, hope, salvation , also could be natural landscapes that reflect the title of the album or situations in the real life where the phrase is reflected BENEATH THE QUIET RAIN (GOD) , the primary focus is what happens when we hear the name of God , the market is for people who believe in God , referent to the letters i would like to see fonts more modern, however I will be here to hope see ALL your talent friends god bless you cheers
Nice to have
• natural landscapes with people that represent the concept of the album or actual scene of daily living, also modern fonts,
Should not have
• the moon, the skeleton , dead signals , dark things, satan draws, the chains and the handaxes,etc. reflect the opposite way that i want to proyect in this music i want to proyect through my music is hope, salvation, peace, and the principal objective that is WHAT HAPPEN WHEN I HEAR THE NAME OF GOD when we live in difficult situations

```html
<!DOCTYPE html>
<html lang="es">
<head>
<meta charset="utf-8">
<title>Bajo la Lluvia Serena — Elías Moro</title>
<link rel="stylesheet" href="https://fonts.googleapis.com/css2?family=Raleway:wght@300;400;500&display=swap">
<style>
  :root {
    --page: #ffffff;
    --frame: #ffffff;
    --ink: #141414;
    --shadow: rgba(40, 44, 44, 0.85);
    --lime: #e2e35c;
    --olive: #8f9238;
    --rose: #c8646c;
    --pine: #3d7467;
    --sky: #5cc6df;
    --mist: #93b5ea;
    --sun: #f2ee3a;
    --amber: #f4a020;
    --scarlet: #e8241e;
    --leaf: #c6e83a;
    --green: #2ee043;
    --aqua: #42d8cf;
    --cobalt: #1434df;
  }
  * { margin: 0; padding: 0; box-sizing: border-box; }
  html, body {
    width: 1200px; height: 1000px; overflow: hidden;
    background: var(--page);
  }
  .sheet { position: relative; width: 1200px; height: 1000px; }

  .panel {
    position: absolute;
    top: 242px;
    width: 412px; height: 410px;
    background: var(--frame);
    box-shadow: 14px 16px 14px var(--shadow);
  }
  .panel--front { left: 178px; }
  .panel--back { left: 632px; }

  .artwork {
    position: absolute; inset: 8px 12px 7px 12px;
  }
  .artwork--front {
    background:
      linear-gradient(180deg, rgba(255,255,255,0.25) 0%, rgba(255,255,255,0) 30%),
      linear-gradient(90deg, var(--lime) 0%, var(--olive) 28%, var(--rose) 52%, var(--pine) 68%, var(--sky) 86%, var(--mist) 100%);
  }
  .artwork--back {
    background:
      linear-gradient(180deg, rgba(255,255,255,0.55) 0%, rgba(255,255,255,0) 22%, rgba(255,255,255,0) 85%, rgba(255,255,255,0.4) 100%),
      linear-gradient(90deg, var(--sun) 0%, var(--amber) 22%, var(--scarlet) 48%, var(--leaf) 62%, var(--green) 74%, var(--aqua) 88%, var(--cobalt) 100%);
  }

  .title, .artist, .tracklist, .tracklist-label {
    position: absolute;
    font-family: "Raleway", sans-serif;
    color: var(--ink);
  }
  .title {
    left: 0; right: 0; top: 105px;
    text-align: center;
    font-weight: 300;
    font-size: 27px;
    line-height: 41px;
    letter-spacing: 0.3em;
    padding-left: 0.3em;
  }
  .artist {
    left: 0; right: 0; top: 281px;
    text-align: center;
    font-weight: 400;
    font-size: 21px;
    letter-spacing: 0.36em;
    padding-left: 0.36em;
  }
  .tracklist-label {
    left: 34px; top: 36px;
    font-weight: 500;
    font-size: 15px;
    letter-spacing: 0.3em;
  }
  .tracklist {
    left: 18px; top: 78px;
    list-style: none;
    font-weight: 500;
    font-size: 13px;
    line-height: 23.6px;
    letter-spacing: 0.24em;
    white-space: nowrap;
  }
</style>
</head>
<body>
<main class="sheet">
  <section class="panel panel--front">
    <div class="artwork artwork--front" role="img" aria-label="Watercolour-washed photograph of a musician playing an electric guitar, in yellow, rose and turquoise tones"></div>
    <h1 class="title">BAJO LA LLUVIA<br>SERENA</h1>
    <p class="artist">ELÍAS MORO</p>
  </section>

  <section class="panel panel--back">
    <div class="artwork artwork--back" role="img" aria-label="Dripping rainbow watercolour wash in yellow, orange, red, green, cyan and blue"></div>
    <h2 class="tracklist-label">SONGS:</h2>
    <ol class="tracklist">
      <li>1. BAJO LA LLUVIA SERENA</li>
      <li>2. LUZ EN MI CAMINO</li>
      <li>3. CIELO ABIERTO</li>
      <li>4. AGUA VIVA Y ETERNA</li>
      <li>5. TU PAZ</li>
      <li>6. ESPERANZA</li>
      <li>7. SOL DE LA MAÑANA</li>
      <li>8. TU VOZ ME ALCANZÓ</li>
      <li>9. LUZ EN MI CAMINO (DISCO)</li>
      <li>10. NUEVO AMANECER</li>
    </ol>
  </section>
</main>
</body>
</html>
```